Business card design needed

The company name is Pellwick Architects. We are an architectural company based in Melbourne,Australia that has a mix of client base from health care, commercial office, aged care, multi-residential, single residential and retail. Design type is contemporary.

Suggest the base colours need to be black and white. Please leave an area on the back of the card available for handwritten notes.

Target Market(s)

Generally corporate, aged 30 to 65

Industry/Entity Type

Residential

Contact Information for Business Card

Pellwick Architects
Dane Pellwick
7 Horbury Street
Northvale VIC 3059
T (03) 9572 4016
M 0431 607 295
E dp@pellwickarc.com.au

Logo Text

PA

Logo styles of interest
Emblem Logo
Abstract Logo
Lettermark Logo
Requirements
Must have
• I am having trouble attaching a sketch so would really appreciate your effort to try the following brief.

Black and White (B&W)
Would like different card cutout profile. Logo Example, use the half circle curve of the G to form the left edge of the card with no margin. The A is to sit inside the G, connected to the G by its horizontal. The A has its cross bar and lower right leg removed. Card in black, text in white.

Back of card to be black text on white background with services provided.

Client Focused Service
Architecture and Design
Functional Planning
Town Planning
Feasability Studies
Contract Documentation
Contract Administration
Project Management

Simple elegant text, Ariel or similar
Nice to have
• Integrated logo and card cut-out.

Card base black on front, white on back
Should not have
• Too many colours
Fussy details

```html
<!DOCTYPE html>
<html lang="en">
<head>
<meta charset="utf-8">
<title>Pellwick Architects — Business Card</title>
<link rel="stylesheet" href="https://fonts.googleapis.com/css2?family=Josefin+Sans:wght@300;400&display=swap">
<style>
  :root {
    --paper: #ffffff;
    --card: #000000;
    --ink: #ffffff;
  }
  html, body {
    margin: 0;
    padding: 0;
    width: 1200px;
    height: 708px;
    overflow: hidden;
    background: var(--paper);
  }
  .canvas {
    position: relative;
    width: 1200px;
    height: 708px;
    background: var(--paper);
    font-family: "Josefin Sans", Arial, sans-serif;
    color: var(--ink);
  }
  .card-front {
    position: absolute;
    left: 18px;
    top: 0;
    width: 1182px;
    height: 704px;
    background: var(--card);
  }
  .monogram {
    position: absolute;
    left: 40px;
    top: 270px;
    width: 240px;
    text-align: center;
    font-weight: 300;
    font-size: 140px;
    line-height: 1;
    letter-spacing: 4px;
    color: var(--ink);
  }
  .company-name {
    position: absolute;
    left: 300px;
    top: 336px;
    margin: 0;
    font-weight: 300;
    font-size: 60px;
    line-height: 1;
    letter-spacing: 6px;
    text-transform: uppercase;
    white-space: nowrap;
  }
  .contact {
    position: absolute;
    left: 323px;
    top: 578px;
    width: 600px;
    margin: 0;
    text-align: center;
    font-style: normal;
    font-weight: 300;
    font-size: 28px;
    line-height: 41px;
    white-space: nowrap;
  }
  .contact span { display: block; }
</style>
</head>
<body>
  <div class="canvas">
    <section class="card-front">
      <div class="monogram">PA</div>
      <h1 class="company-name">Pellwick Architects</h1>
      <address class="contact">
        <span class="contact-address">Dane Pellwick 7 Horbury Street Northvale VIC 3059</span>
        <span class="contact-phone">Tel (03) 9572 4016 M 0431 607 295</span>
        <span class="contact-email">Email: dp@pellwickarc.com.au</span>
      </address>
    </section>
  </div>
</body>
</html>
```